Marketing Skill "Workouts"; Design for an e-mail attachment highlighting Marketing training subjects

I am a freelance marketing trainer based in Singapore and need to e-mail out an attachment (probably saved as a PDF) to potential clients showing the training services I offer. These clients are all large blue-chip multinational companies so the attachment needs to look professional/high quality when opened on a computer.

My Company is called "Brightpath Marketing" (logo attached)

I am assuming the size should be A4 one sided colour.

I have attached some files that show best-attempts so far. These contain the key information, but the layouts all still look rather pedestrian. I am looking for something that looks a bit more dynamic but remains clear/easy to read.

Target Market(s)

HR/Marketing managers in multinational firms, mainly consumer goods

Industry/Entity Type

Marketing

Font styles to use
Sans Serif

Colors

Designer to choose colors to be used in the design.

Requirements
Must have
• Must look modern, up-to-date, professional.
Should not have
• Not gimmicky, like a cheap deal

```html
<!DOCTYPE html>
<html lang="en">
<head>
<meta charset="utf-8">
<title>Marketing Skill Workouts – Brightpath Marketing</title>
<link href="https://fonts.googleapis.com/css2?family=Montserrat:wght@300;500;600;700;800&display=swap" rel="stylesheet">
<style>
  :root{
    --stone:#9b9b9b;
    --stone-dark:#8a8a8a;
    --band:rgba(85,85,85,.75);
    --brand-red:#b5202e;
    --deep-red:#9e2a2b;
    --teal:#235a69;
    --key-teal:#2f5f6d;
    --ink:#111;
    --white:#fff;
  }
  *{margin:0;padding:0;box-sizing:border-box}
  html,body{width:1200px;height:834px;overflow:hidden;background:var(--stone)}
  body{font-family:"Montserrat",Arial,sans-serif;position:relative}
  .sheet{position:absolute;inset:0;background:radial-gradient(circle at 30% 40%,#a4a4a4,var(--stone) 55%,var(--stone-dark))}
  .hero-photo{position:absolute;left:0;top:0}

  .title{position:absolute;left:44px;top:40px;color:var(--white)}
  .title-line{display:block;font-weight:300;font-size:56px;line-height:1}
  .title-accent{display:block;font-weight:700;font-size:56px;color:var(--deep-red);margin-top:10px;line-height:1}

  .intro{position:absolute;left:0;top:182px;width:520px;height:80px;background:var(--band);
    color:var(--white);font-weight:600;font-size:15.6px;line-height:21px;padding:10px 4px 0 45px}

  .card{position:absolute;background:var(--white);border:1px solid #7a8a90}
  .card-head{position:absolute;background:var(--brand-red);color:var(--white);font-weight:600;white-space:nowrap}
  .badge{position:absolute;border-radius:50%;background:var(--white);border:11px solid var(--brand-red);
    display:flex;align-items:center;justify-content:center}

  .item{position:absolute;font-size:14.6px;font-weight:600;color:var(--ink);line-height:18px}
  .item.bullet::before{content:"";position:absolute;left:-17px;top:6px;width:6px;height:6px;border-radius:50%;background:var(--brand-red)}

  .topics{left:78px;top:372px;width:280px;height:318px}
  .topics-head{left:32px;top:309px;width:341px;height:65px;font-size:30px;padding:12px 0 0 112px}
  .topics-badge{left:30px;top:302px;width:86px;height:86px}
  .topics .item{left:31px;width:245px}

  .benefits{left:461px;top:404px;width:280px;height:286px}
  .benefits-head{left:420px;top:311px;width:335px;height:97px;font-size:32px;padding:31px 0 0 125px;border-radius:0 8px 0 0}
  .benefits-badge{left:420px;top:306px;width:114px;height:114px}
  .benefits .item{left:31px;width:205px}
  .benefit-icon{position:absolute;left:242px}

  .why-frame{position:absolute;left:0;top:0}
  .why-text{position:absolute;left:894px;top:416px;color:var(--white);font-weight:600;font-size:16.6px;line-height:21px}
  .why-title{color:var(--ink);font-size:34px;font-weight:700;line-height:1.1;margin-bottom:11px}
  .why-line{display:block;white-space:nowrap}
  .why-text b{color:var(--ink);font-weight:700;font-size:18.5px}

  .footer{position:absolute;left:0;top:728px}
  .touch{position:absolute;left:37px;top:745px;color:var(--brand-red);font-weight:700;font-size:42px;line-height:54px}
  .contact{position:absolute;color:var(--white);font-weight:600;font-size:19px;left:522px;line-height:24px}
  .contact.phone{top:752px}
  .contact.mail{top:787px}
  .contact-icon{position:absolute;left:467px}
  .brand{position:absolute;right:20px;top:766px;display:flex;align-items:center;gap:12px;color:var(--ink);font-weight:500;font-size:20px;white-space:nowrap}
  .brand-dot{width:56px;height:56px;border-radius:50%;background:var(--deep-red);flex:none}
</style>
</head>
<body>
<div class="sheet"></div>

<svg class="hero-photo" width="1200" height="834" viewBox="0 0 1200 834">
  <defs>
    <linearGradient id="gymTones" x1="0" y1="0" x2="1" y2="1">
      <stop offset="0" stop-color="#3a5a7e"/>
      <stop offset=".5" stop-color="#2c5e6c"/>
      <stop offset="1" stop-color="#6f7478"/>
    </linearGradient>
  </defs>
  <polygon points="525,0 1200,0 1200,334 840,334" fill="url(#gymTones)" role="img" aria-label="Photo of a man bench pressing a barbell in a gym"/>
  <polyline points="504,0 836,348 1200,348" fill="none" stroke="var(--brand-red)" stroke-width="3"/>
</svg>

<h1 class="title">
  <span class="title-line">Marketing skill</span>
  <span class="title-accent">“Workouts”</span>
</h1>

<p class="intro">No time to learn? Problem solved with 1 day intensive workshops that will drive business growth and motivate your team</p>

<!-- Key topics -->
<div class="card topics">
  <div class="item bullet" style="top:21px">Developing Strong Brand Plans</div>
  <div class="item bullet" style="top:47px">Writing inspiring Briefs/Creative Evaluation</div>
  <div class="item bullet" style="top:91px">Shopper Marketing/Developing Retail Promotions</div>
  <div class="item bullet" style="top:134px">Brilliant Launch Management</div>
  <div class="item" style="top:160px">Improving Marketing R.O.I.</div>
  <div class="item bullet" style="top:185px">Driving Brand Growth without Product Innovation</div>
  <div class="item bullet" style="top:229px">Insight/Concept Development</div>
  <div class="item bullet" style="top:254px">Integrating Digital Channels</div>
  <div class="item bullet" style="top:280px">Creativity and Idea Generation</div>
</div>
<div class="card-head topics-head">Key Topics</div>
<div class="badge topics-badge">
  <svg width="38" height="38" viewBox="0 0 40 40"><circle cx="27" cy="13" r="9" fill="var(--key-teal)"/><circle cx="27" cy="13" r="3.5" fill="#fff"/><path d="M21 19 L5 35 M9 31 l4 4 M13 27 l4 4" stroke="var(--key-teal)" stroke-width="5" stroke-linecap="round"/></svg>
</div>

<!-- Key benefits -->
<div class="card benefits">
  <div class="item bullet" style="top:21px">Latest in world-class thinking/tools/case studies</div>
  <div class="item bullet" style="top:73px">Ability to 'customise' to address your specific business issue</div>
  <div class="item bullet" style="top:145px">Asian context/relevance</div>
  <div class="item bullet" style="top:176px">Take-away 'checklists' to embed behaviours and skills</div>
  <div class="item bullet" style="top:245px">Proven quality</div>

  <svg class="benefit-icon" style="top:28px" width="28" height="28" viewBox="0 0 28 28" fill="none" stroke="var(--brand-red)" stroke-width="2"><rect x="2" y="2" width="24" height="24"/><rect x="7" y="16" width="3" height="6" fill="var(--brand-red)"/><rect x="12" y="12" width="3" height="10" fill="var(--brand-red)"/><rect x="17" y="8" width="3" height="14" fill="var(--brand-red)"/></svg>
  <svg class="benefit-icon" style="top:90px" width="28" height="26" viewBox="0 0 28 26" fill="none" stroke="var(--brand-red)" stroke-width="2"><rect x="2" y="6" width="24" height="18" rx="3"/><path d="M10 6 V2 h8 v4 M2 13 h24 M12 13 v3 h4 v-3"/></svg>
  <svg class="benefit-icon" style="top:138px;left:243px" width="26" height="32" viewBox="0 0 26 32" fill="none" stroke="var(--brand-red)" stroke-width="1.8"><circle cx="13" cy="12" r="9"/><ellipse cx="13" cy="12" rx="4" ry="9"/><path d="M4 12 h18 M13 24 v4 M7 30 h12"/></svg>
  <svg class="benefit-icon" style="top:192px;left:243px" width="26" height="28" viewBox="0 0 26 28" fill="none" stroke="var(--brand-red)" stroke-width="1.8"><rect x="2" y="4" width="18" height="22"/><path d="M6 2 v4 M11 2 v4 M16 2 v4 M6 12 h8 M6 17 h6 M12 22 l11 -14"/></svg>
  <svg class="benefit-icon" style="top:238px;left:241px" width="30" height="30" viewBox="0 0 30 30" fill="none" stroke="var(--brand-red)" stroke-width="2"><circle cx="15" cy="15" r="13"/><path d="M8 15 l5 5 l9 -10"/></svg>
</div>
<div class="card-head benefits-head">Key Benefits</div>
<div class="badge benefits-badge">
  <svg width="48" height="48" viewBox="0 0 40 40"><circle cx="27" cy="13" r="9" fill="var(--key-teal)"/><circle cx="27" cy="13" r="3.5" fill="#fff"/><path d="M21 19 L5 35 M9 31 l4 4 M13 27 l4 4" stroke="var(--key-teal)" stroke-width="5" stroke-linecap="round"/></svg>
</div>

<!-- Why me -->
<svg class="why-frame" width="1200" height="834" viewBox="0 0 1200 834">
  <polyline points="894,398 1144,398 1144,644" fill="none" stroke="var(--ink)" stroke-width="2"/>
  <polyline points="866,428 866,674 1116,674" fill="none" stroke="var(--ink)" stroke-width="2"/>
  <text x="840" y="466" font-family="Montserrat, Arial, sans-serif" font-weight="800" font-size="118" fill="var(--ink)">“</text>
  <text x="1116" y="741" font-family="Montserrat, Arial, sans-serif" font-weight="800" font-size="118" fill="var(--ink)">”</text>
</svg>
<div class="why-text">
  <h2 class="why-title">Why Me?</h2>
  <span class="why-line">The latest thinking, made</span>
  <span class="why-line">practical and actionable.</span>
  <span class="why-line"><b>20 years</b> of business</span>
  <span class="why-line">experience combined with</span>
  <span class="why-line">over 10 years of proven</span>
  <span class="why-line">training/facilitation for</span>
  <span class="why-line">major “blue-chip” clients,</span>
  <span class="why-line">regularly scoring <b>90%+</b></span>
  <span class="why-line"><b>satisfaction</b></span>
</div>

<!-- Footer -->
<svg class="footer" width="1200" height="106" viewBox="0 0 1200 106">
  <rect x="0" y="0" width="1200" height="106" fill="var(--white)"/>
  <polygon points="374,0 828,0 880,106 0,106 0,88 404,88" fill="var(--teal)"/>
</svg>
<div class="touch">Keep in touch</div>
<svg class="contact-icon" style="top:751px" width="26" height="26" viewBox="0 0 24 24"><path fill="#fff" d="M6.6 10.8a15 15 0 0 0 6.6 6.6l2.2-2.2c.3-.3.7-.4 1-.2 1.1.4 2.3.6 3.6.6.6 0 1 .4 1 1V20c0 .6-.4 1-1 1A17 17 0 0 1 3 4c0-.6.4-1 1-1h3.5c.6 0 1 .4 1 1 0 1.3.2 2.5.6 3.6.1.3 0 .7-.2 1z"/></svg>
<div class="contact phone">+65 6000 4120</div>
<svg class="contact-icon" style="top:791px" width="26" height="18" viewBox="0 0 26 18" fill="none" stroke="#fff" stroke-width="1.6"><rect x="1" y="1" width="24" height="16"/><path d="M1 1 l12 9 l12 -9 M1 17 l9 -8 M25 17 l-9 -8"/></svg>
<div class="contact mail">hello@brightpath-marketing.com</div>

<div class="brand"><span>Brightpath Marketing</span><span class="brand-dot"></span></div>
</body>
</html>
```